Brightmoor Auto Care 4x9 Rack Card

Design a 4" wide by 9" tall rack card printed front and back using the copy, logo and images uploaded below. I am also uploading a current flyer so you can see the typestyles we use. I will get the exact name of the font for you ASAP. Also will be uploading some before and after pictures for the back of the rack card

Target Market(s)

Affluent consumers who need their car cleaned and detailed in a meticulous fashion

Requirements
Must have
• Under the logo, put the words...... Premium Steam Detailing & Ceramic Coating.........also put ther following wording on the front side: Get Steamed! We use steam to clean your vehicle helping save millions of gallons of water and protecting our rivers, streams and lakes from runoff.
Nice to have
• a screened back background of hexagons might be nice

```html
<!DOCTYPE html>
<html lang="en">
<head>
<meta charset="utf-8">
<title>Brightmoor Auto Care – Rack Card</title>
<link href="https://fonts.googleapis.com/css2?family=Poppins:wght@400;500;600;700&display=swap" rel="stylesheet">
<style>
:root{
  --green:#5fa045;
  --green-dark:#2f6a2a;
  --green-pale:#b9d3a3;
  --blue:#2e59a6;
  --blue-dark:#1d3a75;
  --blue-pale:#b8c8e6;
  --ink:#1f2a24;
  --grey:#4a4f4c;
  --paper:#ffffff;
  --canvas:#ffffff;
}
*{margin:0;padding:0;box-sizing:border-box}
html,body{width:1145px;height:1200px;overflow:hidden;background:var(--canvas);font-family:"Poppins",sans-serif;color:var(--ink)}
.card{position:absolute;top:60px;width:480px;height:1080px;background:var(--paper);overflow:hidden;box-shadow:0 0 4px rgba(0,0,0,.12)}
.card--front{left:54px}
.card--back{left:611px}
.abs{position:absolute}
.brand{font-weight:600;color:#fff;font-size:15px;letter-spacing:1.5px;text-transform:uppercase;line-height:1.15}
.brand--dark{color:var(--green-dark)}
.hero-title{left:38px;top:130px;color:#fff;font-weight:600;font-size:36px;line-height:38px;text-transform:uppercase}
.hero-copy{left:38px;top:268px;width:300px;color:#fff;font-size:13.4px;line-height:20px}
.phone-pill{height:31px;border-radius:16px;background:linear-gradient(180deg,#3f6fc0,var(--blue-dark));color:#fff;font-weight:600;font-size:16px;display:flex;align-items:center;justify-content:center;box-shadow:0 2px 3px rgba(0,0,0,.25)}
.section-title{font-weight:600;font-size:22px;line-height:25px;text-transform:uppercase;color:var(--ink)}
.icon-circle{width:40px;height:40px;border-radius:50%;background:radial-gradient(circle at 40% 35%,#4f9a3e,var(--green-dark));border:3px solid #fff;box-shadow:0 1px 4px rgba(0,0,0,.3);display:flex;align-items:center;justify-content:center}
.location{left:50px;width:190px}
.location__head{display:flex;align-items:center;gap:16px;font-weight:600;font-size:12.5px}
.location__addr{margin-left:38px;font-size:8.6px;line-height:15px;color:var(--grey);margin-top:6px}
.location__call{margin-left:38px;font-size:8.6px;margin-top:4px;font-weight:600}
.location__call span{color:var(--green-dark);font-weight:400;text-decoration:underline}
.info-head{font-weight:600;font-size:9.5px;line-height:16px;text-transform:uppercase}
.info-list{font-size:8.6px;line-height:15px;color:var(--grey);margin-top:12px}
.quote{font-weight:700;font-size:26px;line-height:35px;text-align:right;text-transform:uppercase;color:var(--green-dark)}
.quote em{font-style:normal;color:var(--green)}
.footer{left:0;top:990px;width:480px;height:90px;background:linear-gradient(180deg,#4f8d3c,#2f6a2a)}
.footer .brand{position:absolute;left:40px;top:14px;font-size:9px;letter-spacing:1px;width:100px}
.footer__contacts{position:absolute;left:40px;top:50px;display:flex;gap:16px;color:#fff;font-size:9.5px;align-items:center}
.footer__contacts span{display:flex;align-items:center;gap:6px}
.footer__copy{position:absolute;left:40px;top:71px;color:#fff;font-size:6.6px}
.price-list{left:50px;top:650px;list-style:none;width:400px}
.price-list li{display:flex;gap:12px;font-size:12.2px;font-weight:500;line-height:18px;margin-bottom:15px}
.price-list li b{color:var(--green);font-weight:500}
.ba{left:39px;top:425px;width:401px;height:189px;display:flex;gap:2px;box-shadow:0 0 3px rgba(0,0,0,.25)}
.ba__photo{flex:1;display:flex;align-items:center;justify-content:center;color:#fff;font-weight:600;font-size:15px}
.ba__photo--before{background:linear-gradient(160deg,#6f706c,#3c3d3b 60%,#8c8a84)}
.ba__photo--after{background:linear-gradient(160deg,#6a6b69,#2f3031 55%,#505254)}
.ceramic-title{left:39px;top:853px;font-weight:500;font-size:17px}
.ceramic-copy{left:39px;top:882px;width:200px;font-size:6.6px;line-height:13.5px;color:var(--grey)}
.hand{flex:none;margin-top:1px}
</style>
</head>
<body>

<!-- FRONT -->
<section class="card card--front">
  <svg class="abs" style="left:0;top:0" width="480" height="620" aria-hidden="true">
    <defs>
      <linearGradient id="heroGreen" x1="0" y1="0" x2="0" y2="1">
        <stop offset="0" stop-color="#6aa84f"/><stop offset="1" stop-color="#4f8f3c"/>
      </linearGradient>
    </defs>
    <polygon points="0,0 480,0 480,364 215,550 0,490" fill="url(#heroGreen)"/>
  </svg>

  <div class="abs brand" style="left:290px;top:46px;width:175px;text-align:right">Brightmoor<br>Auto Care</div>
  <h1 class="abs hero-title">Premium Steam<br>Detailing &amp;<br>Ceramic Coating</h1>
  <p class="abs hero-copy">Get Steamed! We use steam to clean your vehicle helping save millions of gallons of water &amp; protecting our rivers, streams and lakes from runoff.</p>
  <div class="abs phone-pill" style="left:39px;top:365px;width:143px">(555) 014-2200</div>

  <svg class="abs" style="left:0;top:0" width="480" height="720" role="img" aria-label="Hexagon photo cluster: detailer in blue shirt steam cleaning the front grille of a luxury car">
    <defs>
      <polygon id="hexF" points="0,-68 58.9,-34 58.9,34 0,68 -58.9,34 -58.9,-34"/>
      <linearGradient id="photoF" x1="0" y1="0" x2="1" y2="1">
        <stop offset="0" stop-color="#c9c3b2"/><stop offset=".45" stop-color="#3b5a9a"/><stop offset="1" stop-color="#1f3566"/>
      </linearGradient>
    </defs>
    <g stroke="#fff" stroke-width="4" fill="url(#photoF)">
      <use href="#hexF" x="336" y="400"/>
      <use href="#hexF" x="274" y="508"/>
      <use href="#hexF" x="398" y="508"/>
    </g>
    <use href="#hexF" x="336" y="616" fill="var(--green-pale)" stroke="#fff" stroke-width="4"/>
  </svg>

  <div class="abs icon-circle" style="left:42px;top:619px">
    <svg width="16" height="20" viewBox="0 0 16 20" aria-hidden="true"><path d="M8 0C3.6 0 0 3.4 0 7.6 0 13 8 20 8 20s8-7 8-12.4C16 3.4 12.4 0 8 0z" fill="#fff"/><circle cx="8" cy="7.5" r="3" fill="var(--green-dark)"/></svg>
  </div>
  <h2 class="abs section-title" style="left:97px;top:616px">Our<br>Locations</h2>

  <div class="abs location" style="top:686px">
    <div class="location__head"><svg class="hand" width="22" height="14" viewBox="0 0 22 14" aria-hidden="true"><path d="M0 3h5v11H0zM6 4l4-3h10a2 2 0 010 4h-6v8H6z" fill="var(--green-dark)"/></svg>Fairhaven</div>
    <p class="location__addr">1420 Harbor Lane @ The Westgate<br>Market Hall,<br>Fairhaven</p>
    <p class="location__call"><span>Call Us :</span> (555) 018-3300</p>
  </div>
  <div class="abs location" style="top:789px">
    <div class="location__head"><svg class="hand" width="22" height="14" viewBox="0 0 22 14" aria-hidden="true"><path d="M0 3h5v11H0zM6 4l4-3h10a2 2 0 010 4h-6v8H6z" fill="var(--green-dark)"/></svg>Pine Ridge</div>
    <p class="location__addr">52 Alder Road<br>Pine Ridge Village</p>
    <p class="location__call"><span>Call Us :</span> (555) 014-2200</p>
  </div>
  <div class="abs location" style="top:879px">
    <div class="location__head"><svg class="hand" width="22" height="14" viewBox="0 0 22 14" aria-hidden="true"><path d="M0 3h5v11H0zM6 4l4-3h10a2 2 0 010 4h-6v8H6z" fill="var(--green-dark)"/></svg>Millbrook</div>
    <p class="location__addr">318 Kestrel Rd #120<br>Millbrook</p>
    <p class="location__call"><span>Call Us :</span> (555) 019-5500</p>
  </div>

  <div class="abs icon-circle" style="left:265px;top:688px">
    <svg width="18" height="18" viewBox="0 0 24 24" aria-hidden="true"><path d="M6.6 10.8a15 15 0 006.6 6.6l2.2-2.2c.3-.3.7-.4 1-.2 1.1.4 2.3.6 3.6.6.6 0 1 .4 1 1V20c0 .6-.4 1-1 1A17 17 0 013 4c0-.6.4-1 1-1h3.5c.6 0 1 .4 1 1 0 1.3.2 2.5.6 3.6.1.3 0 .7-.2 1z" fill="#fff"/></svg>
  </div>
  <div class="abs" style="left:323px;top:695px">
    <p class="info-head">Call for information<br>&amp; scheduling:</p>
    <p class="info-list">Fairhaven &nbsp;(555) 018-3300<br>Cedar Falls &nbsp;(555) 016-4400<br>Larkspur (555) 014-2200<br>Pine Ridge (555) 014-2200</p>
  </div>

  <p class="abs quote" style="right:40px;top:822px">“<em>Fall in love</em><br><em>with your</em><br>car again!”</p>

  <div class="abs footer">
    <div class="brand">Brightmoor<br>Auto Care</div>
    <div class="footer__contacts">
      <span><svg width="10" height="10" viewBox="0 0 24 24" aria-hidden="true"><path d="M6.6 10.8a15 15 0 006.6 6.6l2.2-2.2c.3-.3.7-.4 1-.2 1.1.4 2.3.6 3.6.6.6 0 1 .4 1 1V20c0 .6-.4 1-1 1A17 17 0 013 4c0-.6.4-1 1-1h3.5c.6 0 1 .4 1 1 0 1.3.2 2.5.6 3.6.1.3 0 .7-.2 1z" fill="#fff"/></svg>(555) 014-2200</span>
      <span><svg width="11" height="11" viewBox="0 0 20 20" aria-hidden="true"><circle cx="10" cy="10" r="8.5" fill="none" stroke="#fff" stroke-width="1.5"/><path d="M1.5 10h17M10 1.5c3 3 3 14 0 17M10 1.5c-3 3-3 14 0 17" fill="none" stroke="#fff" stroke-width="1.3"/></svg>www.brightmoorauto.com</span>
    </div>
    <p class="footer__copy">Copyright © 2022 brightmoorautocare . All Rights Reserved.</p>
  </div>

  <svg class="abs" style="left:300px;top:930px" width="180" height="150" role="img" aria-label="Hexagon photo of detailer polishing a car hood">
    <defs>
      <polygon id="hexS" points="0,-50 43.3,-25 43.3,25 0,50 -43.3,25 -43.3,-25"/>
      <linearGradient id="photoS" x1="0" y1="0" x2="1" y2="1"><stop offset="0" stop-color="#6f87b8"/><stop offset="1" stop-color="#1d2f57"/></linearGradient>
    </defs>
    <g fill="url(#photoS)" stroke="#fff" stroke-width="2" opacity=".95">
      <use href="#hexS" x="90" y="50"/><use href="#hexS" x="45" y="128"/><use href="#hexS" x="135" y="128"/>
    </g>
  </svg>
</section>

<!-- BACK -->
<section class="card card--back">
  <svg class="abs" style="left:0;top:0" width="480" height="470" role="img" aria-label="Honeycomb photo collage: detailer in cap steam cleaning the grille of a silver sports car">
    <defs>
      <polygon id="hexB" points="60,0 30,52 -30,52 -60,0 -30,-52 30,-52"/>
      <polygon id="hexD" points="0,-62 53.7,-31 53.7,31 0,62 -53.7,31 -53.7,-31"/>
      <linearGradient id="photoB" gradientUnits="userSpaceOnUse" x1="0" y1="0" x2="480" y2="330">
        <stop offset="0" stop-color="#cfc2a2"/><stop offset=".4" stop-color="#8a8374"/><stop offset=".6" stop-color="#3a5da3"/><stop offset="1" stop-color="#263a6c"/>
      </linearGradient>
      <clipPath id="combB">
        <use href="#hexB" x="-11" y="62"/><use href="#hexB" x="-11" y="172"/>
        <use href="#hexB" x="85" y="7"/><use href="#hexB" x="85" y="117"/><use href="#hexB" x="85" y="227"/>
        <use href="#hexB" x="179" y="62"/><use href="#hexB" x="179" y="172"/><use href="#hexB" x="179" y="282"/>
        <use href="#hexB" x="277" y="7"/><use href="#hexB" x="277" y="117"/><use href="#hexB" x="277" y="227"/>
        <use href="#hexB" x="373" y="62"/><use href="#hexB" x="373" y="172"/>
        <use href="#hexB" x="469" y="7"/><use href="#hexB" x="469" y="117"/>
      </clipPath>
    </defs>
    <g opacity=".55">
      <use href="#hexD" x="24" y="260" fill="var(--green)"/>
      <use href="#hexD" x="40" y="385" fill="var(--blue-pale)"/>
      <use href="#hexD" x="100" y="360" fill="var(--green-pale)"/>
      <use href="#hexD" x="475" y="230" fill="var(--green-pale)"/>
    </g>
    <rect width="480" height="470" fill="url(#photoB)" clip-path="url(#combB)"/>
  </svg>

  <div class="abs brand brand--dark" style="left:270px;top:348px;width:172px;font-size:17px;text-align:right">Brightmoor<br>Auto Care</div>

  <div class="abs ba" role="img" aria-label="Before and after photos of a truck cabin floor and leather seat">
    <div class="ba__photo ba__photo--before">Before</div>
    <div class="ba__photo ba__photo--after">After</div>
  </div>

  <ul class="abs price-list">
    <li><svg class="hand" width="22" height="14" viewBox="0 0 22 14" aria-hidden="true"><path d="M0 3h5v11H0zM6 4l4-3h10a2 2 0 010 4h-6v8H6z" fill="var(--green-dark)"/></svg><span>Premium Steam Washes starting at <b>$100 and up</b></span></li>
    <li><svg class="hand" width="22" height="14" viewBox="0 0 22 14" aria-hidden="true"><path d="M0 3h5v11H0zM6 4l4-3h10a2 2 0 010 4h-6v8H6z" fill="var(--green-dark)"/></svg><span>Full Steam Detailing starting at <b>$275 and up</b></span></li>
    <li><svg class="hand" width="22" height="14" viewBox="0 0 22 14" aria-hidden="true"><path d="M0 3h5v11H0zM6 4l4-3h10a2 2 0 010 4h-6v8H6z" fill="var(--green-dark)"/></svg><span>Paint Correction (multi-stage polishing) starting at <b>$650 and up</b></span></li>
    <li><svg class="hand" width="22" height="14" viewBox="0 0 22 14" aria-hidden="true"><path d="M0 3h5v11H0zM6 4l4-3h10a2 2 0 010 4h-6v8H6z" fill="var(--green-dark)"/></svg><span>Headlight Restoration - <b>$110</b></span></li>
    <li><svg class="hand" width="22" height="14" viewBox="0 0 22 14" aria-hidden="true"><path d="M0 3h5v11H0zM6 4l4-3h10a2 2 0 010 4h-6v8H6z" fill="var(--green-dark)"/></svg><span>Engine Steam Cleaning - <b>$75</b></span></li>
  </ul>

  <p class="abs quote" style="right:40px;top:810px">“<em>Fall in love</em><br><em>with your</em><br>car again!”</p>

  <h3 class="abs ceramic-title">Ceramic Coating</h3>
  <p class="abs ceramic-copy">Lorem ipsum dolor sit amet, consectetur adipiscing elit, sed do eiusmod tempor incididunt ut labore et dolore magna aliqua. Quis ipsum suspendisse ultrices gravida. Risus</p>
  <div class="abs phone-pill" style="left:39px;top:932px;width:143px">(555) 014-2200</div>

  <div class="abs footer">
    <div class="brand">Brightmoor<br>Auto Care</div>
    <div class="footer__contacts">
      <span><svg width="10" height="10" viewBox="0 0 24 24" aria-hidden="true"><path d="M6.6 10.8a15 15 0 006.6 6.6l2.2-2.2c.3-.3.7-.4 1-.2 1.1.4 2.3.6 3.6.6.6 0 1 .4 1 1V20c0 .6-.4 1-1 1A17 17 0 013 4c0-.6.4-1 1-1h3.5c.6 0 1 .4 1 1 0 1.3.2 2.5.6 3.6.1.3 0 .7-.2 1z" fill="#fff"/></svg>(555) 014-2200</span>
      <span><svg width="11" height="11" viewBox="0 0 20 20" aria-hidden="true"><circle cx="10" cy="10" r="8.5" fill="none" stroke="#fff" stroke-width="1.5"/><path d="M1.5 10h17M10 1.5c3 3 3 14 0 17M10 1.5c-3 3-3 14 0 17" fill="none" stroke="#fff" stroke-width="1.3"/></svg>www.brightmoorauto.com</span>
    </div>
    <p class="footer__copy">Copyright © 2022 brightmoorautocare . All Rights Reserved.</p>
  </div>

  <svg class="abs" style="left:300px;top:930px" width="180" height="150" role="img" aria-label="Hexagon photo of detailer polishing a car hood">
    <g fill="url(#photoS)" stroke="#fff" stroke-width="2" opacity=".95">
      <use href="#hexS" x="90" y="50"/><use href="#hexS" x="45" y="128"/><use href="#hexS" x="135" y="128"/>
    </g>
  </svg>
</section>

</body>
</html>
```